Business Card Design Project

Use our current logo. Clean design.

Industry/Entity Type

Business

Requirements
Must have
• Marisela DUBRANCQ
M. Law
Managing Partner

Alpenvorsa AG
Kornhalmweg 214
CH-3097 Liebefeld

M. +41 79 412 56 27
T. +41 31 928 44 10
F. +41 31 928 44 19

m.dubrancq@alpenvorsa-example.com
www.alpenvorsa-example.com

```html
<!DOCTYPE html>
<html lang="de">
<head>
<meta charset="utf-8">
<title>Alpenvorsa AG – Visitenkarte</title>
<link rel="stylesheet" href="https://fonts.googleapis.com/css2?family=Arimo:wght@400&display=swap">
<style>
  :root {
    --stage: #e9e6e0;
    --card-front: #ffffff;
    --card-back-top: #3a3a3a;
    --card-back-bottom: #161616;
    --ink: #1a1a1a;
    --accent: #e3141b;
    --back-mark: #111111;
    --rule: #9a9a9a;
  }
  * { box-sizing: border-box; margin: 0; padding: 0; }
  html, body {
    width: 1200px;
    height: 800px;
    overflow: hidden;
    background: var(--stage);
    font-family: "Arimo", Arial, sans-serif;
    color: var(--ink);
  }
  .stage {
    width: 1200px;
    height: 800px;
    display: flex;
    align-items: center;
    justify-content: center;
    gap: 70px;
  }
  .card {
    width: 340px;
    height: 595px;
    box-shadow: 0 10px 30px rgba(0, 0, 0, 0.25);
    position: relative;
  }
  .card--front {
    background: var(--card-front);
    text-align: center;
    padding-top: 58px;
  }
  .brand {
    display: inline-flex;
    flex-direction: column;
    align-items: center;
  }
  .brand__name {
    font-size: 28px;
    letter-spacing: 3px;
    text-transform: uppercase;
    color: var(--ink);
  }
  .brand__rule {
    width: 200px;
    height: 1px;
    background: var(--rule);
    margin-top: 10px;
  }
  .holder__name {
    margin-top: 62px;
    font-size: 17px;
    color: var(--accent);
    text-transform: uppercase;
    letter-spacing: 0.3px;
  }
  .block {
    font-size: 15px;
    line-height: 19px;
  }
  .holder__role { margin-top: 22px; }
  .address { margin-top: 24px; }
  .contact { margin-top: 24px; text-align: left; display: inline-block; }
  .contact__label { display: inline-block; width: 22px; }
  .web { margin-top: 24px; }
  .card--back {
    background: radial-gradient(ellipse at 40% 20%, var(--card-back-top), var(--card-back-bottom) 85%);
  }
  .back-brand {
    position: absolute;
    right: 28px;
    bottom: 40px;
    font-size: 22px;
    letter-spacing: 3px;
    text-transform: uppercase;
    color: var(--back-mark);
  }
</style>
</head>
<body>
  <main class="stage">
    <section class="card card--front" aria-label="Vorderseite">
      <div class="brand">
        <span class="brand__name">Alpenvorsa</span>
        <span class="brand__rule"></span>
      </div>
      <p class="holder__name">Marisela DUBRANCQ</p>
      <p class="block holder__role">M. Law<br>Managing Partner</p>
      <p class="block address">Alpenvorsa AG<br>Kornhalmweg 214<br>CH-3097 Liebefeld</p>
      <p class="block contact">
        <span class="contact__label">M.</span>+41 79 412 56 27<br>
        <span class="contact__label">T.</span>+41 31 928 44 10<br>
        <span class="contact__label">F.</span>+41 31 928 44 19
      </p>
      <p class="block web">m.dubrancq@alpenvorsa-example.com<br>www.alpenvorsa-example.com</p>
    </section>
    <section class="card card--back" aria-label="Rückseite">
      <span class="back-brand">Alpenvorsa</span>
    </section>
  </main>
</body>
</html>
```